Erklär-Flyer für Gutschein-Ankauf-Service Bonkarten-Profi.de
Zielgruppe
Auf http://www.bonkarten-profi.de/ bieten wir u.a. den Service an, ungenutzte Geschenkkarten von großen Händlern wie z.B. Technoplatz, Vandoro, WOLM, usw. direkt gegen Bargeld einzutauschen. Diesen Service wollen wir nun in einem Flyer vorstellen.
Die Zielgruppe des zu erstellenden Flyers sollen vor allem Mitarbeiter bei Firmen z.B. Auto Verkäufer sein, die von Ihrem Arbeitgeber als Prämie Geschenkgutscheine als Incentive erhalten und diese aber lieber in Bargeld umtauschen würden.
Das Wunschszenario wäre: Wir schicken den Flyer zusammen mit einem Anschreiben an die jeweiligen Firmen. Der/diejenige die den Brief und Flyer entgegennimmt, erkennt den Sinn und Nutzen und gibt den Flyer an Ihre Kollegen weiter bzw. hängt ihn ans schwarze Brett etc.
Aufgabenstellung
Gestaltet werden soll ein 3 Schritte Falz-Flyer (z.B. 6-seitiger Altarfalz Fensterfalz) angelehnt an das bisherige Design auf Bonkarten-Profi.de (nicht zwingend 100%, gerne auch eigene Ideen). Auf der Außenseite nur kurz in einem Satz um was es geht und auf der Innenseite dann am Besten in 3 Schritten erklärt, wie einfach der Umtausch von Gutscheinen in Bargeld ist.
Das Wichtigste ist die "Bequemlichkeit, Einfachheit, kein Aufwand", am zweitwichtigsten ist "Sicherheit, Seriosität" (Unsere Seite gibt es schon seit 2008 und wir wurden bereits im KRT vorgestellt).
Verteilung des Falt-Flyer als Brief mit der Post. Wenn der Brief geöffnet wird ist der zu erreichende Optimal Zustand, dass der Flyer von der Person, die den Brief öffnet, z.B. ans "schwarze Brett" gehängt wird als Info bzw. eine Art Anleitung.

```html
<!DOCTYPE html>
<html lang="de">
<head>
<meta charset="utf-8">
<title>Bonkarten-Profi.de – Falzflyer</title>
<link href="https://fonts.googleapis.com/css2?family=Ubuntu:wght@400;500&display=swap" rel="stylesheet">
<style>
  :root {
    --green: #8bb12a;
    --blue: #105a8e;
    --red: #e2574b;
    --grey-bg: #eef0f1;
    --grey-text: #555b60;
    --white: #ffffff;
    --fold: #c9cdd0;
  }
  * { box-sizing: border-box; margin: 0; padding: 0; }
  html, body { width: 1200px; height: 1200px; overflow: hidden; background: #ffffff; }
  body { font-family: "Ubuntu", sans-serif; position: relative; }

  .spread {
    position: absolute; left: 30px; width: 1140px; height: 381px;
    background: linear-gradient(180deg, #f4f5f6 0%, #e8eaec 100%);
    box-shadow: 0 1px 4px rgba(0,0,0,.25);
    overflow: hidden;
  }
  .spread--outside { top: 190px; }
  .spread--inside { top: 630px; }

  .panel { position: absolute; top: 0; width: 380px; height: 381px; }
  .panel + .panel { border-left: 1px dashed var(--fold); }
  .panel--1 { left: 0; } .panel--2 { left: 380px; } .panel--3 { left: 760px; }

  .url {
    position: absolute; right: 24px; bottom: 22px;
    font-size: 10px; font-weight: 500; color: var(--grey-text);
  }

  /* outside */
  .photo-cards {
    position: absolute; left: 0; top: 0; width: 760px; height: 250px;
    background:
      linear-gradient(170deg, rgba(255,255,255,0) 55%, #eef0f1 80%),
      linear-gradient(90deg, #e6a2c8 0%, #c55a8f 15%, #6fae43 35%, #e8c23b 50%, #dfe2e4 70%, #f3f4f5 100%);
  }
  .intro-box {
    position: absolute; left: 24px; top: 243px; width: 332px; height: 88px;
    background: var(--green); color: var(--white); border-radius: 3px;
    padding: 12px 12px; font-size: 12.5px; line-height: 1.55;
  }
  .intro-box p + p { margin-top: 12px; }

  .brand {
    position: absolute; color: var(--blue); font-weight: 500;
    line-height: 1; display: flex; align-items: center; gap: 7px;
  }
  .brand::after {
    content: ""; width: 12px; height: 12px; border-radius: 50%; background: var(--green);
  }
  .brand--panel2 { left: 36px; top: 322px; font-size: 22px; }
  .brand--cover { right: 22px; top: 42px; font-size: 22px; }

  .cta-badge {
    position: absolute; left: 220px; top: 210px; width: 126px; height: 126px;
    border-radius: 50%; background: #dcdfe1; box-shadow: 0 2px 6px rgba(0,0,0,.25);
    display: flex; align-items: center; justify-content: center;
  }
  .cta-badge span {
    width: 108px; height: 108px; border-radius: 50%; background: var(--red);
    color: var(--white); font-size: 14px; font-weight: 500; line-height: 1.25;
    display: flex; align-items: center; justify-content: center; text-align: center;
    transform: rotate(-12deg);
  }

  .photo-cover {
    position: absolute; inset: 0;
    background:
      radial-gradient(ellipse at 40% 35%, #d7a98a 0%, #a9765a 18%, rgba(169,118,90,0) 38%),
      linear-gradient(160deg, #e9ecef 0%, #d4d8db 40%, #e9e3a6 80%, #f1e9a6 100%);
  }
  .claim-box {
    position: absolute; left: 24px; top: 243px; width: 226px; height: 88px;
    background: var(--blue); color: var(--white); border-radius: 3px;
    padding: 11px 15px; font-size: 15px; line-height: 1.6;
  }
  .benefits {
    position: absolute; left: 262px; top: 243px; width: 118px; height: 88px;
    background: var(--green); color: var(--white); border-radius: 3px;
    padding: 10px 0 0 16px; list-style: none; font-size: 15px; line-height: 1.6;
  }
  .benefits li { display: flex; align-items: center; gap: 8px; }
  .benefits svg { width: 14px; height: 14px; }

  /* inside */
  .step-head { position: absolute; left: 24px; top: 24px; display: flex; gap: 6px; }
  .step-head span {
    background: var(--green); color: var(--white); font-size: 21px;
    height: 36px; line-height: 36px; padding: 0 12px; border-radius: 2px;
  }
  .step-photo { position: absolute; left: 0; top: 79px; width: 380px; height: 184px; }
  .step-photo--1 { background: linear-gradient(100deg, #b57a57 0%, #e9c5aa 35%, #3a3d42 60%, #d5e2ef 100%); }
  .step-photo--2 { background: linear-gradient(160deg, #f5f6f7 0%, #c99f86 35%, #5b6f86 70%, #2f3a48 100%); }
  .step-photo--3 { background: radial-gradient(ellipse at 50% 45%, #c68d6b 0%, #7e4c34 30%, #ffffff 65%); }
  .step-text {
    position: absolute; left: 24px; top: 281px; width: 334px; height: 54px;
    background: var(--white); color: var(--grey-text); border-radius: 2px;
    padding: 8px 10px; font-size: 12.5px; line-height: 1.6;
  }
</style>
</head>
<body>

<section class="spread spread--outside" aria-label="Außenseite">
  <div class="photo-cards" role="img" aria-label="Stapel bunter Geschenkkarten"></div>

  <div class="panel panel--1">
    <div class="intro-box">
      <p>Haben Sie uneingelößte Gutscheine herumliegen?<br>Machen Sie diese bequem und sicher zu Geld!</p>
      <p>Und das in nur drei einfachen Schritten...</p>
    </div>
    <span class="url">bonkarten-profi.de</span>
  </div>

  <div class="panel panel--2">
    <div class="brand brand--panel2">Bonkarten Profi</div>
    <div class="cta-badge"><span>JETZT<br>Gutscheine<br>zu Geld<br>machen!</span></div>
    <span class="url">bonkarten-profi.de</span>
  </div>

  <div class="panel panel--3">
    <div class="photo-cover" role="img" aria-label="Lächelnde Frau hält einen Gutschein in der Hand"></div>
    <div class="brand brand--cover">Bonkarten Profi</div>
    <div class="claim-box">Wir machen Ihre ungenutzen Gutscheine zu Bargeld!</div>
    <ul class="benefits">
      <li><svg viewBox="0 0 16 16"><circle cx="8" cy="8" r="8" fill="#fff"/><path d="M4.5 8.3l2.4 2.3 4.6-4.8" stroke="#8bb12a" stroke-width="2" fill="none"/></svg>Bequem</li>
      <li><svg viewBox="0 0 16 16"><circle cx="8" cy="8" r="8" fill="#fff"/><path d="M4.5 8.3l2.4 2.3 4.6-4.8" stroke="#8bb12a" stroke-width="2" fill="none"/></svg>Einfach</li>
      <li><svg viewBox="0 0 16 16"><circle cx="8" cy="8" r="8" fill="#fff"/><path d="M4.5 8.3l2.4 2.3 4.6-4.8" stroke="#8bb12a" stroke-width="2" fill="none"/></svg>Sicher</li>
    </ul>
    <span class="url">bonkarten-profi.de</span>
  </div>
</section>

<section class="spread spread--inside" aria-label="Innenseite">
  <div class="panel panel--1">
    <div class="step-head"><span>1</span><span>Anbieter wählen</span></div>
    <div class="step-photo step-photo--1" role="img" aria-label="Frau am Laptop mit geöffneter Webseite"></div>
    <p class="step-text">Gehen Sie auf bonkarten-profi.de und suchen Sie den entsprechenden Anbieter heraus.</p>
    <span class="url">bonkarten-profi.de</span>
  </div>
  <div class="panel panel--2">
    <div class="step-head"><span>2</span><span>Daten eingeben</span></div>
    <div class="step-photo step-photo--2" role="img" aria-label="Hände tippen auf einer Tastatur"></div>
    <p class="step-text">Melden Sie sich kostenlos bei uns an und geben Sie Ihre Gutschein-Informationen ein.</p>
    <span class="url">bonkarten-profi.de</span>
  </div>
  <div class="panel panel--3">
    <div class="step-head"><span>3</span><span>Geld aufs Konto</span></div>
    <div class="step-photo step-photo--3" role="img" aria-label="Begeisterte Frau mit Geldscheinen"></div>
    <p class="step-text">Einfach ausdrucken und abschicken. Das Geld erhalten Sie direkt auf Ihr Konto.</p>
    <span class="url">bonkarten-profi.de</span>
  </div>
</section>

</body>
</html>
```